Business Card design for consulting company

We are a small consulting company (Valmor Consulting) just starting out and need a business card design with a simple yet slick logo. We provide client focused consultancy support to manage and advise on procurement and acquisition projects for private businesses. Most of our projects are conducted for large well established companies and involve a fair degree of international work, so we would like to reflect that in the design. A large part of the business is also understanding client needs and then connecting them to, or sourcing the right solutions. So we would like to communicate our professionalism, an international focus and our willingness to provide tailored client solutions.

Target Market(s)

Generally we deal with middle to senior executive levels at large companies or with some high wealth private clients/companies. Mostly a conservative group so we want to project a sharp, professional and international image.

Industry/Entity Type

Consulting

Requirements
Must have
• Looking for a simple double sided business card design. Need to have our business name (Valmor Consulting), a person''s name and position title, and our company contact details. Also need a logo that would also convey the international nature of our consultancy.

```html
<!DOCTYPE html>
<html lang="en">
<head>
<meta charset="utf-8">
<title>Valmor Consulting – Business Card</title>
<link href="https://fonts.googleapis.com/css2?family=Questrial&display=swap" rel="stylesheet">
<style>
  :root {
    --page: #ffffff;
    --card-light: #e4e4e4;
    --card-mid: #cfcfcf;
    --card-edge: #b1b1b1;
    --ink: #3f3f3f;
    --ink-soft: #4a4a4a;
    --rule: #8c8c8c;
    --mark-blue: #1e88e8;
  }
  * { margin: 0; padding: 0; box-sizing: border-box; }
  html, body {
    width: 1200px; height: 394px; overflow: hidden;
    background: var(--page);
    font-family: "Questrial", "Century Gothic", sans-serif;
    color: var(--ink);
  }
  .canvas { position: relative; width: 1200px; height: 394px; }
  .card {
    position: absolute; top: 32px;
    width: 554px; height: 332px;
    background: radial-gradient(ellipse 62% 58% at 50% 48%, var(--card-light) 0%, var(--card-mid) 55%, var(--card-edge) 100%);
    box-shadow: 3px 3px 4px rgba(0,0,0,0.35);
  }
  .card--front { left: 28px; }
  .card--back { left: 614px; }

  .brand-mark {
    position: absolute; border-radius: 50%;
    width: 130px; height: 130px;
    background: var(--mark-blue);
  }
  .card--front .brand-mark { left: 214px; top: 68px; }
  .card--back .brand-mark { left: 76px; top: 93px; }

  .front-name {
    position: absolute; left: 0; width: 100%; top: 226px;
    text-align: center; font-size: 44px; line-height: 1;
    color: var(--ink);
  }

  .divider {
    position: absolute; left: 242px; top: 50px;
    width: 1px; height: 234px; background: var(--rule);
  }
  .details { position: absolute; left: 270px; top: 58px; }
  .details .company { font-size: 29px; line-height: 1; color: var(--ink); }
  .details .person { margin-top: 13px; font-size: 18px; line-height: 1; color: var(--ink-soft); }
  .details .role { font-size: 12px; font-style: italic; line-height: 1.15; color: var(--ink-soft); }
  .details .lines { font-size: 12px; line-height: 14px; color: var(--ink-soft); }
  .details .address { margin-top: 15px; }
  .details .phone { margin-top: 14px; }
  .details .web { margin-top: 14px; }
</style>
</head>
<body>
<div class="canvas">
  <section class="card card--front">
    <div class="brand-mark" aria-hidden="true"></div>
    <div class="front-name">Valmor Consulting</div>
  </section>

  <section class="card card--back">
    <div class="brand-mark" aria-hidden="true"></div>
    <div class="divider"></div>
    <div class="details">
      <div class="company">Valmor Consulting</div>
      <div class="person">Daniel Hart</div>
      <div class="role">Senior Consultant</div>
      <div class="lines address">Address Line 1<br>Address Line 2<br>Address Line 3</div>
      <div class="lines phone">07700900461</div>
      <div class="lines web">www.valmorconsulting.com<br>daniel@valmorconsulting.com</div>
    </div>
  </section>
</div>
</body>
</html>
```